Architecture firm needing a business card

We need a business card design for a new company based in the US called "Pellmore Architecture". Seeking minimalist designs that have a creativity/design feel but must be clean and professional. Please refer to the logo attached.

Target Market(s)

Real Estate Investors, Home Builders and Construction Firms.

Industry/Entity Type

Architecture

Contact Information for Business Card

Standard US size business cards. Would like to have some sort of graphic on the back side of the card - nothing that is too loud but something that may catch your attention. More or less grayscale colors that are in line with the logo colors (navy and greys essentially). Additional colors maybe accepted if blended properly (earthtones), but might be difficult to accomplish and maintain the clean/minimalist look.

Requirements
Must have
• Clean Lines
Nice to have
• some sort of graphics, would like to have something creative on the back side of the card
Should not have
• nothing too busy, cluttered or overwhelming.

```html
<!DOCTYPE html>
<html lang="en">
<head>
<meta charset="utf-8">
<title>Pellmore Architecture – Business Card</title>
<link href="https://fonts.googleapis.com/css2?family=Lato:wght@400;700&display=swap" rel="stylesheet">
<style>
  :root {
    --page-bg: #1c1c1e;
    --navy: #24507f;
    --navy-deep: #1a3f68;
    --navy-light: #3a6797;
    --paper: #ffffff;
    --paper-shade: #eceef0;
    --ink-light: #e8eef5;
    --icon-ink: #24507f;
  }
  * { box-sizing: border-box; margin: 0; padding: 0; }
  html, body {
    width: 1200px; height: 864px; overflow: hidden;
    background: var(--page-bg);
    font-family: "Lato", Arial, sans-serif;
  }
  .stage {
    width: 1200px; height: 864px;
    display: flex; flex-direction: column;
    align-items: center; justify-content: center; gap: 56px;
  }
  .card {
    width: 560px; height: 320px;
    border-radius: 4px; overflow: hidden;
    box-shadow: 0 10px 30px rgba(0,0,0,.5);
    position: relative;
  }

  /* Back */
  .card-back {
    background: linear-gradient(160deg, var(--navy-light) 0%, var(--navy) 55%, var(--navy-deep) 100%);
    display: flex; align-items: center; justify-content: center;
  }
  .card-back .brand-name {
    color: var(--ink-light);
    font-size: 38px; font-weight: 400; letter-spacing: 2px;
    text-transform: uppercase;
  }

  /* Front */
  .card-front { background: var(--paper); display: flex; flex-direction: column; }
  .front-top {
    height: 170px;
    background: linear-gradient(180deg, var(--paper) 0%, var(--paper-shade) 100%);
    display: flex; align-items: center; justify-content: center;
  }
  .front-top .brand-name {
    color: var(--navy);
    font-size: 30px; font-weight: 400; letter-spacing: 2px;
    text-transform: uppercase;
  }
  .front-band {
    flex: 1;
    background: linear-gradient(160deg, var(--navy-light) 0%, var(--navy) 50%, var(--navy-deep) 100%);
    color: var(--ink-light);
    padding: 14px 0 0;
  }
  .person {
    text-align: center; font-size: 14px; font-weight: 700;
    margin-bottom: 14px;
  }
  .person .divider { margin: 0 10px; font-weight: 400; }
  .person .role { font-size: 12px; }
  .details { display: flex; justify-content: center; gap: 28px; }
  .address { text-align: right; font-size: 12px; line-height: 17px; }
  .contacts { list-style: none; font-size: 12.5px; line-height: 17px; }
  .contacts li { display: flex; align-items: center; gap: 10px; }
  .contacts svg { width: 13px; height: 13px; flex: none; }
</style>
</head>
<body>
<main class="stage">

  <section class="card card-back" aria-label="Card back">
    <span class="brand-name">Pellmore Architecture</span>
  </section>

  <section class="card card-front" aria-label="Card front">
    <div class="front-top">
      <span class="brand-name">Pellmore Architecture</span>
    </div>
    <div class="front-band">
      <p class="person">Tan Wei Lin<span class="divider">|</span><span class="role">Managing Director</span></p>
      <div class="details">
        <address class="address" style="font-style:normal">
          18 Harlow Street<br>Crestfield Building<br>#12-00<br>Singapore 061442
        </address>
        <ul class="contacts">
          <li>
            <svg viewBox="0 0 14 14"><rect width="14" height="14" rx="3" fill="#e8eef5"/><path d="M4 3.5l1.6-.4.9 2-1 .8a5 5 0 0 0 2.6 2.6l.8-1 2 .9-.4 1.6C8 10 4 6 4 3.5z" fill="#24507f"/></svg>
            (0000) 555-210
          </li>
          <li>
            <svg viewBox="0 0 14 14"><rect width="14" height="14" rx="3" fill="#e8eef5"/><rect x="4.5" y="2.5" width="5" height="9" rx="1" fill="none" stroke="#24507f" stroke-width="1.2"/></svg>
            (0000) 555-210
          </li>
          <li>
            <svg viewBox="0 0 14 14"><rect width="14" height="14" rx="3" fill="#e8eef5"/><rect x="3" y="4" width="8" height="6" fill="#24507f"/><path d="M3 4l4 3 4-3" fill="none" stroke="#e8eef5" stroke-width=".9"/></svg>
            hello@pellmorearch.com
          </li>
          <li>
            <svg viewBox="0 0 14 14"><rect width="14" height="14" rx="3" fill="#e8eef5"/><circle cx="7" cy="7" r="3.6" fill="none" stroke="#24507f" stroke-width="1"/><path d="M3.4 7h7.2M7 3.4c-1.6 2-1.6 5.2 0 7.2M7 3.4c1.6 2 1.6 5.2 0 7.2" fill="none" stroke="#24507f" stroke-width=".8"/></svg>
            www.pellmorearch.com
          </li>
        </ul>
      </div>
    </div>
  </section>

</main>
</body>
</html>
```